Personal training and nutrition business needs business card design

We need a business card that outlays our services and invites potential customers to join our team and take the first step to a healthier and more enjoyable life. We cater for any level of fitness and specialize in weight loss and conditioning, strength training, muscle gain and strength endurance. Whether you are just starting off or need some help getting to the next level of your journey we are here to get the job done.
We specialize in one on one or one on two personal training sessions and each program will be custom made to suit individual fitness goals of our clients

```html
<!DOCTYPE html>
<html lang="en">
<head>
<meta charset="utf-8">
<title>Pulse &amp; Pace – Business Card</title>
<link href="https://fonts.googleapis.com/css2?family=Lato:wght@700;900&family=Arimo:wght@400&family=Oswald:wght@500&display=swap" rel="stylesheet">
<style>
  :root{
    --backdrop:#242424;
    --paper:#ffffff;
    --ink:#111111;
    --purple:#8a4fa6;
    --purple-top:#ae64a8;
    --purple-bottom:#764a9c;
    --white:#ffffff;
  }
  *{margin:0;padding:0;box-sizing:border-box}
  html,body{width:1065px;height:1200px;overflow:hidden;background:var(--backdrop)}
  .canvas{position:relative;width:1065px;height:1200px}

  .card{position:absolute;box-shadow:3px 3px 4px rgba(0,0,0,.6)}
  .card-front{left:292px;top:218px;width:582px;height:362px;background:var(--paper);border-radius:0 181px 181px 0}
  .card-back{left:263px;top:623px;width:582px;height:363px;border-radius:181px 0 0 181px;
    background:linear-gradient(to bottom,var(--purple-top),var(--purple-bottom))}

  .person{position:absolute;left:28px;top:90px}
  .person-name{font:700 24px/1 "Lato",sans-serif;color:var(--purple);letter-spacing:-.3px}
  .person-role{font:400 17px/1 "Arimo",sans-serif;color:var(--ink);margin-top:4px}

  .contacts{position:absolute;left:28px;top:150px;list-style:none}
  .contacts li{display:flex;align-items:center;gap:5px;font:400 16.5px/21px "Arimo",sans-serif;color:var(--ink)}
  .contacts svg{width:16px;height:16px;flex:none}
  .accent{color:var(--purple)}

  .address{position:absolute;left:28px;top:226px;font:400 16.5px/21px "Arimo",sans-serif;color:var(--ink)}

  .brand{position:absolute;display:flex;flex-direction:column;align-items:center;text-align:center}
  .brand-front{left:300px;top:98px;width:210px}
  .brand-back{left:160px;top:70px;width:270px}
  .brand-mark{border-radius:50%}
  .brand-front .brand-mark{width:56px;height:56px;background:var(--purple);margin-bottom:18px}
  .brand-back .brand-mark{width:72px;height:72px;background:var(--white);margin-bottom:26px}
  .brand-name{font:900 34px/1 "Lato",sans-serif;letter-spacing:1px}
  .brand-front .brand-name{color:var(--ink)}
  .brand-back .brand-name{color:var(--white);font-size:44px}
  .brand-tagline{font:500 8.5px/1 "Oswald",sans-serif;letter-spacing:.6px;margin-top:10px}
  .brand-front .brand-tagline{color:var(--purple)}
  .brand-back .brand-tagline{color:var(--white);font-size:10.5px;margin-top:14px}
</style>
</head>
<body>
<div class="canvas">

  <section class="card card-front">
    <div class="person">
      <h1 class="person-name">DANIEL HARLOW</h1>
      <p class="person-role">Managing Director</p>
    </div>
    <ul class="contacts">
      <li>
        <svg viewBox="0 0 16 16" aria-hidden="true"><path d="M4 2l2 3-1.3 1.3a8 8 0 0 0 5 5L11 10l3 2-1.5 2.2C7.5 14.5 1.5 8.5 1.8 3.5z" fill="none" stroke="#8a4fa6" stroke-width="1.5" stroke-linejoin="round"/></svg>
        044-555 010 220
      </li>
      <li>
        <svg viewBox="0 0 16 16" aria-hidden="true"><rect x="0.5" y="3" width="15" height="10" fill="#8a4fa6"/><path d="M0.5 3l7.5 6 7.5-6M0.5 13l5.5-5M15.5 13l-5.5-5" fill="none" stroke="#fff" stroke-width="1"/></svg>
        hello@pulsepace.com
      </li>
      <li>
        <svg viewBox="0 0 16 16" aria-hidden="true"><g fill="none" stroke="#8a4fa6" stroke-width="1.2"><circle cx="8" cy="8" r="7"/><ellipse cx="8" cy="8" rx="3" ry="7"/><path d="M1 8h14M2 4.5h12M2 11.5h12"/></g></svg>
        www.<span class="accent">pulsepace</span>.com
      </li>
    </ul>
    <p class="address">18, Larkspur Avenue<br>20715, Eastvale</p>

    <div class="brand brand-front">
      <span class="brand-mark"></span>
      <p class="brand-name">PULSE &amp;<br>PACE</p>
      <p class="brand-tagline">PERSONAL TRAINING.&nbsp; NUTRITION. MOTIVATION</p>
    </div>
  </section>

  <section class="card card-back">
    <div class="brand brand-back">
      <span class="brand-mark"></span>
      <p class="brand-name">PULSE &amp;<br>PACE</p>
      <p class="brand-tagline">PERSONAL TRAINING.&nbsp; NUTRITION. MOTIVATION</p>
    </div>
  </section>

</div>
</body>
</html>
```